Tobias Wrenfield - Cinematographer

NEED:
I'm looking for a sleek, professional, modern business card that will give give the recipient the impression that they can trust their production will go smoothly by hiring me. I will bring creativity and knowledge to their shoot, so that we can create powerful images.
I am looking for a card with a strong style and design ethos that could be expanded to a website and a full visual/graphic/design entity for me.
ABOUT ME:
I am a mid-twenties cinematographer, I work on music video, narrative short, commercial, and corporate projects. I blend the science and artistry of cameras and filmmaking to tell a story. I'm an artist, a technician, and a manager.
DESIGN:
I like sleek, simple design. Black, dark grays, white, dark navy, steel blues, I love cyan, but also cyan and red. I am not a fan of earthy tones. I generally prefer modern, san-serif fonts over serifs. My old logo was based on an aperture, a multi-blade device at the back of a lens that controls how much light passes through, but I made it with so many colors, that it doesn't necessarily lend itself to a specific color-scheme or design ethos. I liked that the aperture design provided a sense of the technical requirements of my job. I'm a fan of matte business cards, but am open to plenty of specialty print processes to make an outstanding card.
ATTACHED FILES:
My Old Rainbox Aperture Logo, plus a few designs I've tried playing around with, but am not tied to. I AM OPEN TO NEW DESIGNS, DO NOT FEEL TIED TO THIS.
**I've pulled my old logo down from the attached files, and instead attached other business cards I like, so as not to mislead you where I would like to go.
INFO:
Name: Tobias Wrenfield
Job: Cinematographer
Email: tkwrenfield@quillbox.example
Phone: 503.618.2907
Website: tobiaswrenfield.example
Updates
I'm adding some images of other cards that I like, and removing my old logo, since I'm looking for something new, and don't want that old logo to push anyone a certain direction.

```html
<!DOCTYPE html>
<html lang="en">
<head>
<meta charset="utf-8">
<title>Tobias Wrenfield – Business Card</title>
<link rel="stylesheet" href="https://fonts.googleapis.com/css2?family=Aldrich&display=swap">
<style>
  :root {
    --backdrop: #d9dadc;
    --card: #f4f4f4;
    --ink: #111111;
    --name-grey: #6e6e6e;
    --detail-grey: #5c5c5c;
    --paper-white: #ffffff;
  }
  * { margin: 0; padding: 0; box-sizing: border-box; }
  html, body {
    width: 1200px;
    height: 900px;
    overflow: hidden;
    background: var(--backdrop);
    font-family: "Aldrich", sans-serif;
  }
  .canvas {
    position: relative;
    width: 1200px;
    height: 900px;
  }
  .card {
    position: absolute;
    left: 260px;
    width: 680px;
    height: 388px;
    background: var(--card);
    box-shadow: 0 6px 18px rgba(0, 0, 0, 0.12);
  }
  .card--front { top: 52px; }
  .card--back { top: 462px; }

  /* Front */
  .monogram-disc {
    position: absolute;
    left: 50%;
    top: 50%;
    width: 168px;
    height: 168px;
    margin: -84px 0 0 -84px;
    border-radius: 50%;
    background: var(--ink);
    display: flex;
    flex-direction: column;
    align-items: center;
    justify-content: center;
    color: var(--paper-white);
    font-size: 19px;
    line-height: 1.3;
    letter-spacing: 3px;
    text-transform: uppercase;
    text-align: center;
  }

  /* Back */
  .identity {
    position: absolute;
    left: 170px;
    top: 78px;
  }
  .identity__name {
    font-size: 34px;
    letter-spacing: 5px;
    color: var(--name-grey);
    text-transform: uppercase;
    white-space: nowrap;
  }
  .identity__role {
    margin-top: 4px;
    font-size: 11px;
    letter-spacing: 2.5px;
    color: var(--ink);
    text-transform: uppercase;
  }
  .contact {
    position: absolute;
    left: 70px;
    top: 190px;
    display: grid;
    grid-template-columns: 100px auto;
    row-gap: 9px;
    font-size: 10px;
    letter-spacing: 1.8px;
    text-transform: uppercase;
  }
  .contact__label { color: var(--ink); }
  .contact__value { color: var(--detail-grey); }
</style>
</head>
<body>
<main class="canvas">
  <section class="card card--front" aria-label="Card front">
    <div class="monogram-disc">
      <span>Tobias</span>
      <span>Wrenfield</span>
    </div>
  </section>

  <section class="card card--back" aria-label="Card back">
    <div class="identity">
      <h1 class="identity__name">Tobias Wrenfield</h1>
      <p class="identity__role">Cinematographer</p>
    </div>
    <dl class="contact">
      <dt class="contact__label">Email</dt>
      <dd class="contact__value">tkwrenfield@quillbox.example</dd>
      <dt class="contact__label">Phone</dt>
      <dd class="contact__value">503.618.2907</dd>
      <dt class="contact__label">Website</dt>
      <dd class="contact__value">tobiaswrenfield.example</dd>
    </dl>
  </section>
</main>
</body>
</html>
```